Billboard Design for Modern Dispensary

Hello!
We need a eye-catching 12' x 24' billboard designed for a very successful, modern cannabis dispensary on the Oregon coast, United States. Because of rules, we cannot have any marijuana leafs or other cannabis related images (flower, joints, smoke, etc). We can use the words "Shop" or "Dispensary" - we cannot use the words "cannabis", "marijuana".

Some ideas we had are 3 words stacked on left or center of billboard - maybe across bottom we have horizontal logo and the following words - “South of bridge in Depoe Bay”
Another idea is to have a small bubble in bottom/top corner with image of our dog (face only) - with some words around it - like "BONUS Shop Dog" or "Cute Shop Dog" or "Best Shop Dog" or "Friendly Staff"

here's some 3 word examples:
ENJOY
YOUR
TRIP

or

FEEL
GOOD
JUST
AHEAD

or

GOOD
VIBES
ONLY

or

GOOD
TIMES
CHILL
VIBES

I have attached our logo. I have also included a stacked logo version (vertical, not horizontal). the formats are .EPS and .PDF - the logos were created in Affinity Design 2.x.

Our website is coralnook.net if you want to see more images, etc about our dispensary.

Artwork Requirements:
The billboard is 12' tall x 25' wide
The artwork needs to be 1”=1’ @ 300dpi
Please add 6” of bleed all around so your total artwork is 13”x26”
Final deliverable should be .Ai file.

Font styles to use
Sans Serif

Colors
0054AA
0677BA
7BADD7
CADEEF
E8F1F8

Requirements
Nice to have
• See the project description - we included some ideas to consider.
Should not have
• No cannabis images, like flower, cannabis leaves, paraphenlia, cartridges, joints, etc.

```html
<!DOCTYPE html>
<html lang="en">
<head>
<meta charset="utf-8">
<title>Sleep Better Tonight – Billboard</title>
<link href="https://fonts.googleapis.com/css2?family=Montserrat:wght@400;800&display=swap" rel="stylesheet">
<style>
  :root {
    --stage: #1b1713;
    --blue-deep: #0070b5;
    --blue-mid: #3f8fd0;
    --blue-light: #9dc2e8;
    --brand-blue: #3a9ad9;
    --ink: #111111;
    --white: #ffffff;
  }
  html, body {
    margin: 0;
    padding: 0;
    width: 1021px;
    height: 1200px;
    overflow: hidden;
    background: var(--stage);
  }
  .canvas {
    position: relative;
    width: 1021px;
    height: 1200px;
  }
  .billboard {
    position: absolute;
    left: 30px;
    top: 360px;
    width: 960px;
    height: 480px;
    display: flex;
  }
  .billboard__message {
    width: 555px;
    height: 100%;
    background: linear-gradient(180deg, var(--blue-light) 0%, var(--blue-mid) 45%, var(--blue-deep) 100%);
    display: flex;
    flex-direction: column;
    justify-content: center;
    padding-left: 38px;
    box-sizing: border-box;
  }
  .headline {
    margin: 0;
    font-family: "Montserrat", sans-serif;
    font-weight: 800;
    font-size: 86px;
    line-height: 92px;
    color: var(--white);
    letter-spacing: 1px;
  }
  .headline span { display: block; }
  .headline__line--soft { filter: blur(3px); }
  .headline__line--softer { filter: blur(6px); }
  .billboard__brand {
    flex: 1;
    background: var(--white);
    display: flex;
    flex-direction: column;
    align-items: center;
    justify-content: center;
    gap: 22px;
  }
  .brand-dot { display: block; }
  .brand-name {
    font-family: "Montserrat", sans-serif;
    font-weight: 400;
    font-size: 54px;
    color: var(--brand-blue);
    letter-spacing: 1px;
    margin: 0;
  }
</style>
</head>
<body>
  <div class="canvas">
    <section class="billboard">
      <div class="billboard__message">
        <h1 class="headline">
          <span class="headline__line">SLEEP</span>
          <span class="headline__line headline__line--soft">BETTER</span>
          <span class="headline__line headline__line--softer">TONIGHT</span>
        </h1>
      </div>
      <div class="billboard__brand">
        <svg class="brand-dot" width="124" height="124" viewBox="0 0 124 124" aria-hidden="true">
          <circle cx="62" cy="62" r="56" fill="none" stroke="var(--brand-blue)" stroke-width="8"/>
        </svg>
        <p class="brand-name">CORAL NOOK</p>
      </div>
    </section>
  </div>
</body>
</html>
```